Stationary for Beauty and Spa School

Create a business card, letterhead and envelopes (primarily #10 envelope with and without window and catalog envelope) for a beauty and wellness school in Miami, Fl. We offer 8 different programs of study and need an eye catching look. Looking for a combination of modern yet sophisticated. Nothing corporate or business looking. Would like to have a look and feel that is similar (or incorporates aspects) of a new website we will be launching in the next 30 days (screen shot attached.)

The final design should communicate style and elegance in a down to earth and friendly way. We strive to provide our students with quality education, friendly and amicable staff and experienced instructors.
Updates

Hello. FYI, in order to print an aesthetically appealing business card, we would like to print them (the business cards) using silk printing method, with spot UV coating (on some elements, maybe the logo, or depending on the design) and die cuts. Please think of this when preparing your design.

Only 1 day left, please submit your designs for selection. Thanks

Target Market(s)

Adults 18-49 years who are mostly interested in beauty and fashion. Need a youthful & modern look, yet sophisticated and elegant.

Industry/Entity Type

School

Colors
e34197
6b449b
add136
f79021

Requirements
Must have
• Similar look and feel as website (see attached screen shot)
Same look and feel of website (see attached screenshot)
Logo
Address: 5216 SW 3rd Avenue. Miami, Fl 33155
Telephone: 305-514-9382
Fax: 786-420-5163
website/url: www.luminora.edu
incorporate Photo of blonde model (attached)
Nice to have
• Tag line: "Beautify your future." Also, maybe two-sided business card. Would be nice if we could mention our programs (maybe in the back of the card). Below are the program offerings (names cannot be changed but order is irrelevant)... Cosmetology, Barber, Spa Therapy, Massage Therapy, Makeup Artistry, Skin Care, Manicure, Pedicure & Nail Extensions, Full Specialist.

A design with text plus a beautiful photo of a model is appealing. Attached to the files is a sample of a cover for a student handbook we have created. You should use the photo of the blonde model (attached) in your design. The original (quality) version of this stock photograph has been uploaded.

Also would be nice to request clients to follow us on facebook and instagram by including the icons.
Should not have
• A corporate or business look. We are a vocational school teaching beauty and spa programs and we like our advertising to have a look that resembles the industry. We do not want a very serious look or snobby feel.

```html
<!DOCTYPE html>
<html lang="en">
<head>
<meta charset="utf-8">
<title>Luminora School of Beauty — Stationery</title>
<link rel="stylesheet" href="https://fonts.googleapis.com/css2?family=Open+Sans:wght@400;600;700&display=swap">
<style>
  :root {
    --magenta: #e0188f;
    --pink: #e34197;
    --purple: #7b2e9e;
    --violet: #6b449b;
    --ink-blue: #2f2f9c;
    --ink: #111111;
    --paper: #ffffff;
    --window: #a7a7ab;
    --backdrop: #ece8ef;
    --body-font: "Open Sans", Arial, sans-serif;
  }
  * { box-sizing: border-box; margin: 0; padding: 0; }
  html, body { width: 1200px; height: 1000px; overflow: hidden; }
  body { background: var(--backdrop); font-family: var(--body-font); color: var(--ink); }
  .canvas { position: relative; width: 1200px; height: 1000px; overflow: hidden; }

  .piece { position: absolute; background: var(--paper); overflow: hidden;
           box-shadow: 0 6px 18px rgba(40, 20, 60, 0.18); }
  .piece > svg.art { position: absolute; inset: 0; width: 100%; height: 100%; }

  .wordmark { position: absolute; font-family: var(--body-font); font-weight: 700;
              color: var(--ink); line-height: 1; letter-spacing: 0.5px; }
  .wordmark .name { display: block; font-size: 1em; }
  .wordmark .sub { display: block; font-size: 0.34em; letter-spacing: 1px; margin-top: 4px; }

  /* Business card front */
  .card-front { left: 240px; top: 60px; width: 420px; height: 260px;
    background: radial-gradient(ellipse at center, var(--violet) 0%, var(--purple) 35%, var(--magenta) 90%); }
  .card-front .wordmark { left: 150px; top: 108px; font-size: 30px; }

  /* Business card back */
  .card-back { left: 690px; top: 60px; width: 420px; height: 260px; }
  .card-back .wordmark { left: 48px; top: 18px; font-size: 30px; }
  .card-back .programs { position: absolute; left: 40px; top: 78px; list-style: none;
    font-size: 11.5px; line-height: 1.38; }
  .card-back .contact { position: absolute; left: 236px; top: 22px; width: 178px;
    font-size: 9.5px; font-weight: 700; line-height: 1.55; }

  /* Envelopes */
  .envelope { left: 90px; width: 560px; height: 280px; }
  .envelope.plain { top: 350px; }
  .envelope.windowed { top: 660px; height: 300px; }
  .envelope .wordmark { font-size: 30px; }
  .envelope.plain .wordmark { left: 300px; top: 130px; }
  .envelope.windowed .wordmark { left: 300px; top: 120px; }
  .envelope .address-window { position: absolute; left: 70px; top: 190px; width: 290px; height: 80px;
    border-radius: 12px; background: var(--window); }

  /* Letterhead */
  .letterhead { left: 690px; top: 350px; width: 450px; height: 610px; }
  .letterhead .wordmark { left: 22px; top: 12px; font-size: 24px; }
  .letterhead .letter-body { position: absolute; left: 36px; top: 160px; width: 384px;
    font-size: 12.5px; line-height: 1.42; text-align: center; }
  .letterhead .letter-body p + p { margin-top: 16px; }
  .letterhead .letter-contact { position: absolute; left: 222px; top: 462px;
    font-size: 9.5px; line-height: 1.45; font-weight: 600; }
</style>
</head>
<body>
<main class="canvas">

  <section class="piece card-front" aria-label="Business card, front">
    <div class="wordmark"><span class="name">Luminora</span><span class="sub">SCHOOL OF BEAUTY</span></div>
  </section>

  <section class="piece card-back" aria-label="Business card, back">
    <svg class="art" viewBox="0 0 420 260" preserveAspectRatio="none">
      <defs>
        <linearGradient id="backWave" x1="0" y1="0" x2="0" y2="1">
          <stop offset="0" stop-color="#7b2e9e"/><stop offset="1" stop-color="#e0188f"/>
        </linearGradient>
        <linearGradient id="artTone" x1="0" y1="0" x2="1" y2="0">
          <stop offset="0" stop-color="#e34197" stop-opacity="0.55"/><stop offset="1" stop-color="#8d7fb5" stop-opacity="0.55"/>
        </linearGradient>
      </defs>
      <path d="M420,0 L420,260 L320,260 C360,240 395,215 380,185 C365,150 395,120 380,80 C372,55 400,30 420,0 Z" fill="url(#backWave)"/>
      <rect role="img" aria-label="Decorative illustration area in pink and lilac" x="205" y="120" width="130" height="95" fill="url(#artTone)"/>
    </svg>
    <div class="wordmark"><span class="name">Luminora</span><span class="sub">SCHOOL OF BEAUTY</span></div>
    <div class="contact">
      Address: 5216 SW 3rd Avenue.<br>Miami, Fl 33155<br>
      Telephone: 305-514-9382<br>
      Fax: 786-420-5163<br>
      website/url: www.luminora.edu
    </div>
    <ul class="programs">
      <li>- Cosmetology</li><li>-Barber</li><li>-Spa Therapy</li><li>-Massage Therapy</li>
      <li>-Makeup Artistry</li><li>-Skin Care</li><li>-Manicure</li>
      <li>-Pedicure &amp; Nail Extensions</li><li>-Full Specialist</li>
    </ul>
  </section>

  <section class="piece envelope plain" aria-label="Number 10 envelope">
    <svg class="art" viewBox="0 0 560 280" preserveAspectRatio="none">
      <defs>
        <linearGradient id="envGrad1" x1="0" y1="0" x2="1" y2="0">
          <stop offset="0" stop-color="#e0188f"/><stop offset="0.55" stop-color="#b1208f"/><stop offset="1" stop-color="#7b2e9e"/>
        </linearGradient>
      </defs>
      <rect width="560" height="280" fill="url(#envGrad1)"/>
      <path d="M0,62 C60,48 110,88 180,78 C260,66 300,36 380,56 C430,68 470,52 500,60 C485,110 520,140 490,180 C465,215 490,250 455,280 L0,280 Z" fill="#fff"/>
      <path d="M0,28 C70,18 120,62 190,52 C270,42 320,14 400,34 C440,44 470,36 500,42" fill="none" stroke="#2f2f9c" stroke-width="8" opacity="0.85"/>
      <path d="M530,0 C538,70 526,140 537,212" fill="none" stroke="#2f2f9c" stroke-width="7" opacity="0.8"/>
    </svg>
    <div class="wordmark"><span class="name">Luminora</span><span class="sub">SCHOOL OF BEAUTY</span></div>
  </section>

  <section class="piece envelope windowed" aria-label="Number 10 window envelope">
    <svg class="art" viewBox="0 0 560 300" preserveAspectRatio="none">
      <defs>
        <linearGradient id="envGrad2" x1="0" y1="0" x2="1" y2="0">
          <stop offset="0" stop-color="#e0188f"/><stop offset="0.55" stop-color="#b1208f"/><stop offset="1" stop-color="#7b2e9e"/>
        </linearGradient>
      </defs>
      <rect width="560" height="300" fill="url(#envGrad2)"/>
      <path d="M0,85 C60,70 110,108 180,96 C260,84 300,60 380,76 C430,86 470,66 500,62 C485,120 525,150 492,195 C465,235 495,270 460,300 L0,300 Z" fill="#fff"/>
      <path d="M0,68 C70,52 120,88 190,77 C270,65 320,45 400,58 C440,64 470,54 500,56" fill="none" stroke="#2f2f9c" stroke-width="8" opacity="0.85"/>
      <path d="M513,0 C521,60 507,120 520,172" fill="none" stroke="#2f2f9c" stroke-width="7" opacity="0.8"/>
    </svg>
    <div class="wordmark"><span class="name">Luminora</span><span class="sub">SCHOOL OF BEAUTY</span></div>
    <div class="address-window"></div>
  </section>

  <section class="piece letterhead" aria-label="Letterhead">
    <svg class="art" viewBox="0 0 450 610" preserveAspectRatio="none">
      <defs>
        <linearGradient id="lhGrad" x1="0" y1="0" x2="1" y2="0">
          <stop offset="0" stop-color="#e0188f"/><stop offset="1" stop-color="#7b2e9e"/>
        </linearGradient>
      </defs>
      <rect width="450" height="60" fill="url(#lhGrad)"/>
      <path d="M0,66 C120,60 240,72 450,54" fill="none" stroke="#2f2f9c" stroke-width="4" opacity="0.85"/>
      <rect role="img" aria-label="Blue swirl ornament in the header" x="250" y="44" width="90" height="50" fill="#2f2f9c" opacity="0.18"/>
      <path d="M0,560 C140,552 300,566 450,548 L450,610 L0,610 Z" fill="url(#lhGrad)"/>
      <path d="M0,556 C140,548 300,560 450,542" fill="none" stroke="#2f2f9c" stroke-width="4" opacity="0.85"/>
      <rect role="img" aria-label="Blue swirl ornament in the footer" x="80" y="505" width="90" height="50" fill="#2f2f9c" opacity="0.18"/>
    </svg>
    <div class="wordmark"><span class="name">Luminora</span><span class="sub">SCHOOL OF BEAUTY</span></div>
    <div class="letter-body">
      <p>Luminora School of Beauty offers quality education in the field of beauty Arts and Sciences through a planned curriculum and adequate instructors, in a learning environment that acts as an occupational model. Here we will not just teach you a career, but we will make every possible endeavor to make you the best in your field.</p>
      <p>Need a little more re-assurance that we are the school for you? Luminora is accredited by the National Council of Beauty Arts Schools and licensed by the State Board for Career Education. In addition, we offer financial aid programs (to those who qualify), small classes, and job placement assistance to all graduates.</p>
    </div>
    <div class="letter-contact">
      Address: 5216 SW 3rd Avenue. Miami, Fl 33155<br>
      Telephone: 305-514-9382<br>
      Fax: 786-420-5163<br>
      website/url: www.luminora.edu
    </div>
  </section>

</main>
</body>
</html>
```